Harborline Crest Insurance Services

we are a high end insurance agency we specialize on Auto | Home | Business | Life looking for something professional and luxuries at the same time. if you guys need anything else please let me know.

Auto | Home | Business | Life must be under logo on the back with black background.

i want the back part to be black with our gold logo on it.

Target Market(s)

Auto | Home | Business | Life

Industry/Entity Type

Insurance Broker

Contact Information for Business Card

My logo is gold so a black in the back would be nice.

Font styles to use
Serif

Colors
000000

Requirements
Must have
• Big logo on the back with black background.

```html
<!DOCTYPE html>
<html lang="en">
<head>
<meta charset="utf-8">
<title>Harborline Crest Insurance Services – Business Card</title>
<link rel="stylesheet" href="https://fonts.googleapis.com/css2?family=Cinzel:wght@400;600&family=Open+Sans:wght@400&display=swap">
<style>
  :root {
    --gold: #fbbb12;
    --ink-dark: #0c0c0c;
    --ink-mid: #2a2a2a;
    --ink-light: #565656;
    --text-light: #ffffff;
    --page: #ffffff;
  }
  html, body {
    margin: 0;
    width: 1007px;
    height: 1200px;
    overflow: hidden;
    background: var(--page);
  }
  .canvas { position: relative; width: 1007px; height: 1200px; }
  .card {
    position: absolute;
    left: 53px;
    width: 819px;
    height: 469px;
    overflow: hidden;
    background: radial-gradient(ellipse 90% 110% at 78% 62%, var(--ink-light) 0%, var(--ink-mid) 45%, var(--ink-dark) 100%);
  }
  .card--front { top: 53px; }
  .card--back { top: 597px; background: radial-gradient(ellipse 75% 95% at 55% 55%, var(--ink-light) 0%, var(--ink-mid) 50%, var(--ink-dark) 100%); }
  .card__art { position: absolute; inset: 0; }

  .brand-name {
    position: absolute;
    margin: 0;
    font-family: "Cinzel", serif;
    font-weight: 600;
    color: var(--gold);
    text-align: center;
    line-height: 1.15;
  }
  .card--front .brand-name { left: 18px; top: 176px; width: 270px; font-size: 27px; }
  .card--front .brand-name span { display: block; font-size: 13.5px; letter-spacing: 3.5px; }
  .card--back .brand-name { left: 0; right: 0; top: 305px; font-size: 42px; }
  .card--back .brand-name span { display: block; font-size: 18px; letter-spacing: 7px; margin-top: 4px; }

  .contact-list { position: absolute; right: 22px; top: 216px; margin: 0; padding: 0; list-style: none; }
  .contact-item {
    display: flex; align-items: center; justify-content: flex-end;
    height: 42px; margin-bottom: 20px;
    color: var(--text-light);
  }
  .contact-text { text-align: right; margin-right: 14px; font-size: 15px; line-height: 22px; }
  .contact-text--serif { font-family: "Cinzel", serif; font-size: 16px; line-height: 21px; text-align: left; }
  .contact-text--sans { font-family: "Open Sans", sans-serif; }
  .contact-icon {
    width: 38px; height: 38px; flex: none;
    border: 2px solid var(--text-light);
    display: flex; align-items: center; justify-content: center;
  }
  .contact-icon svg { width: 26px; height: 26px; }

  .web-line {
    position: absolute; left: 0; right: 0; top: 425px;
    display: flex; align-items: center; justify-content: center; gap: 20px;
    font-family: "Cinzel", serif; font-size: 23px; color: var(--text-light);
  }
  .dots { display: flex; align-items: center; gap: 8px; }
  .dot { border-radius: 50%; background: var(--text-light); }
  .dot--xs { width: 6px; height: 6px; }
  .dot--s { width: 11px; height: 11px; }
  .dot--m { width: 17px; height: 17px; }
  .dot--l { width: 24px; height: 24px; }
</style>
</head>
<body>
<main class="canvas">

  <section class="card card--front" aria-label="Business card front">
    <svg class="card__art" viewBox="0 0 819 469" aria-hidden="true">
      <path d="M100 469 C230 260 400 160 562 120 C420 170 280 270 175 469 Z" fill="var(--gold)"/>
      <path d="M205 469 C270 360 350 290 410 255 C360 300 300 370 240 469 Z" fill="var(--gold)"/>
    </svg>

    <h1 class="brand-name">Harborline Crest<span>Insurance Services</span></h1>

    <ul class="contact-list">
      <li class="contact-item">
        <div class="contact-text contact-text--serif">YOUR CITY ADDRESS<br>Street Location, City, Country</div>
        <div class="contact-icon">
          <svg viewBox="0 0 26 26"><path d="M3 13 L13 4 L23 13 H20 V23 H6 V13 Z" fill="#fff"/><rect x="11" y="15" width="5" height="5" fill="#333"/></svg>
        </div>
      </li>
      <li class="contact-item">
        <div class="contact-text contact-text--serif">hello@harborlinecrest.com</div>
        <div class="contact-icon">
          <svg viewBox="0 0 26 26"><rect x="2" y="6" width="22" height="15" fill="#fff"/><path d="M2 6 L13 15 L24 6" fill="none" stroke="#333" stroke-width="1.5"/></svg>
        </div>
      </li>
      <li class="contact-item">
        <div class="contact-text contact-text--sans">+1 555 0142 1800<br>+1 555 0198 0009</div>
        <div class="contact-icon">
          <svg viewBox="0 0 26 26"><rect x="7" y="2" width="12" height="22" rx="2" fill="none" stroke="#fff" stroke-width="2"/><rect x="9" y="5" width="8" height="14" fill="#fff"/></svg>
        </div>
      </li>
      <li class="contact-item">
        <div class="contact-text contact-text--sans">WWW.HARBORLINECREST.COM</div>
        <div class="contact-icon">
          <svg viewBox="0 0 26 26" fill="none" stroke="#fff" stroke-width="1.5"><circle cx="13" cy="13" r="10.5"/><ellipse cx="13" cy="13" rx="4.5" ry="10.5"/><path d="M2.5 13 H23.5 M4.5 7.5 H21.5 M4.5 18.5 H21.5 M13 2.5 V23.5"/></svg>
        </div>
      </li>
    </ul>
  </section>

  <section class="card card--back" aria-label="Business card back">
    <svg class="card__art" viewBox="0 0 819 469" aria-hidden="true">
      <ellipse cx="410" cy="234" rx="430" ry="270" fill="none" stroke="var(--gold)" stroke-width="38"/>
    </svg>

    <h2 class="brand-name">Harborline Crest<span>Insurance Services</span></h2>

    <div class="web-line">
      <div class="dots"><span class="dot dot--xs"></span><span class="dot dot--s"></span><span class="dot dot--m"></span><span class="dot dot--l"></span></div>
      <span class="web-address">WWW.HARBORLINECREST.COM</span>
      <div class="dots"><span class="dot dot--l"></span><span class="dot dot--m"></span><span class="dot dot--s"></span><span class="dot dot--xs"></span></div>
    </div>
  </section>

</main>
</body>
</html>
```